Design für Zeitungsanzeige hochwertige Betten
Zielgruppe
Ruhepunkt Sana verkauft hochwertige Bettsystem für schmerzfreies Liegen und Schlafen. Die Kunden (40+) kommen in das Geschäft, weil sie Rückenschmerzen haben und nicht gut schlafen können. Dort werden Sie individuell beraten. Ruhepunkt Sana hat einen Expertenstatus rum um das Thema Liegen und Schlafen, da Sie maßgeschneiderte Matratzen mit Hilfe von Liegedruckmessung anbieten. Die Produkte sind frei von Chemie und Pestiziden, was positiv zum guten Schlaf beiträgt. Somit sind die Produkte auch sehr hochwertig, aber auch kostspielig.
Aufgabenstellung
Gern einmal auf die Seite:
http://www.ruhepunkt-lindenau.de/traumbetten/
http://www.ruhepunkt-sana.com/betten/
-Vorher / nachher Bilder sind sehr effektvoll
-Unbedingt in die Anzeigen nehmen: Adresse- Logo Firma, "Ergonomische Betten" soll mit auf der Anzeige sein und vom Stil ähnlich zu der Schuhanzeige aufgebaut sein.
- gerne auch Unten mit GUTSCHEIN und einer Schere: Kostenlose Liegedruck-Messung
- Zielgruppe 40+
- ein Bett im Hintergrund würde sinnmachen, wenn eine Person davor steht und sich den Rücken hält.
- In der Art wollen wir auch die Anzeige haben. Gut wäre wenn eine ältere Dame zusehen ist, die genau der Zielgruppe entspricht.
Allgemeines:
- Die hohe Qualität der Produkte soll im Vordergrund stehen und die richtige Zielgruppe mit dem passenden Kleingeld ansprechen.
- Das Ruhepunkt Sana Logo muss zusehen sein und auffallen, da dieses sich bei den Menschen einprägen soll.
- Kunden sollen aufgefordert werden zu Ruhepunkt Sana ins Geschäft zu kommen und Ruhepunkt Sana als Experte und Berater soll im Vordergrund stehen.
- Adresse mit Ort muss zusehen sein.
Eine Zeitungsanzeige 4-farbig
Maße: querformat 5*9 cm (und vllt hochformat 4,5*14cm)

```html
<!DOCTYPE html>
<html lang="de">
<head>
<meta charset="utf-8">
<title>Ruhepunkt Sana – Anzeige Ergonomische Betten</title>
<link rel="stylesheet" href="https://fonts.googleapis.com/css2?family=Lato:wght@400;700;900&family=Caveat:wght@700&display=swap">
<style>
  :root {
    --maroon: #6b2225;
    --green: #6faa3c;
    --ink: #1a1a1a;
    --white: #ffffff;
    --photo-light: #f4f4f4;
    --photo-mid: #cfcfcf;
    --dash: #333333;
  }
  html, body { margin: 0; padding: 0; overflow: hidden; }
  body {
    width: 842px; height: 1200px; background: var(--white);
    position: relative; font-family: "Lato", Arial, sans-serif;
  }
  .ad {
    position: absolute; left: 63px; width: 707px; height: 392px;
    border: 1.5px dashed var(--dash); box-sizing: border-box; overflow: hidden;
  }
  .ad--landscape-a { top: 115px; }
  .ad--landscape-b { top: 612px; }
  .ad svg { display: block; width: 707px; height: 392px; }
  .brand { font-weight: 400; font-size: 46px; fill: var(--maroon); }
  .headline { font-weight: 900; }
  .hl-green { fill: var(--green); }
  .hl-maroon { fill: var(--maroon); }
  .cta { font-weight: 900; font-size: 17px; fill: var(--ink); }
  .address { font-weight: 700; font-size: 26px; fill: var(--white); }
  .phone { font-weight: 900; font-size: 24px; fill: var(--white); }
  .voucher-line { font-size: 15px; fill: var(--white); }
  .voucher-line .voucher-label { font-weight: 900; }
  .tag { font-weight: 900; font-size: 20px; fill: var(--ink); letter-spacing: .5px; }
  .tag-spaced { font-weight: 700; font-size: 17px; fill: var(--white); letter-spacing: 2.5px; }
  .voucher-title { font-weight: 900; font-size: 22px; fill: var(--white); }
  .voucher-sub { font-size: 15px; fill: var(--ink); }
  .slogan { font-family: "Caveat", "Comic Sans MS", cursive; font-weight: 700; font-size: 27px; fill: var(--white); }
  .scissors { fill: none; stroke: var(--ink); stroke-width: 2; }
  .scissors--light { stroke: var(--white); }
</style>
</head>
<body>

<section class="ad ad--landscape-a" aria-label="Anzeige Ruhepunkt Sana, Variante mit Gutschein unten">
  <svg viewBox="0 0 707 392" xmlns="http://www.w3.org/2000/svg">
    <defs>
      <linearGradient id="photoFadeA" x1="0" x2="1">
        <stop offset="0" stop-color="var(--white)"/>
        <stop offset=".35" stop-color="var(--photo-light)"/>
        <stop offset="1" stop-color="var(--photo-mid)"/>
      </linearGradient>
      <linearGradient id="bandTopA" x1="0" x2="1">
        <stop offset="0" stop-color="var(--green)" stop-opacity="0"/>
        <stop offset=".4" stop-color="var(--green)"/>
        <stop offset="1" stop-color="var(--green)"/>
      </linearGradient>
      <linearGradient id="bandCtaA" x1="0" x2="1">
        <stop offset="0" stop-color="var(--green)"/>
        <stop offset=".7" stop-color="var(--green)"/>
        <stop offset="1" stop-color="var(--green)" stop-opacity="0"/>
      </linearGradient>
    </defs>

    <rect class="photo" x="290" y="0" width="417" height="392" fill="url(#photoFadeA)" role="img" aria-label="Foto: Frau auf dem Bett sitzend, die sich den schmerzenden Rücken hält"/>
    <rect x="370" y="0" width="337" height="47" fill="url(#bandTopA)"/>
    <text class="tag" x="677" y="31" text-anchor="end">ERGONOMISCHE BETTEN</text>

    <text class="brand" x="37" y="118">Ruhepunkt Sana</text>

    <text class="headline" x="30" y="182"><tspan class="hl-green" font-size="46">Na,</tspan><tspan class="hl-green" font-size="32"> mal </tspan><tspan class="hl-maroon" font-size="42">wieder</tspan></text>
    <text class="headline hl-maroon" x="30" y="227" font-size="52">schlecht</text>
    <text class="headline hl-green" x="30" y="268" font-size="40">geschlafen?</text>

    <path d="M0,286 H370 C395,286 415,300 405,322 H0 Z" fill="url(#bandCtaA)"/>
    <path class="wave" d="M0,322 C220,328 360,318 450,278 C545,238 630,233 707,226 V392 H0 Z" fill="var(--maroon)"/>
    <text class="cta" x="30" y="310">DANN KOMMEN SIE ZU UNS!</text>

    <circle cx="597" cy="160" r="65" fill="var(--maroon)"/>
    <text class="slogan" transform="translate(597,160) rotate(-12)" text-anchor="middle"><tspan x="0" y="-4">Wir nehmen</tspan><tspan x="0" y="24">uns Zeit!</tspan></text>

    <text class="address" x="679" y="284" text-anchor="end">Lindenallee 8</text>
    <text class="address" x="679" y="318" text-anchor="end">23840 Lindenau</text>
    <text class="phone" x="679" y="364" text-anchor="end">04531 48 26 90</text>

    <text class="voucher-line" x="47" y="364"><tspan class="voucher-label">GUTSCHEIN:</tspan> KOSTENLOSE LIEGEDRUCK-MESSUNG</text>

    <g class="scissors scissors--light" transform="translate(4,326) scale(.85)" aria-hidden="true">
      <circle cx="6" cy="32" r="5"/><circle cx="20" cy="32" r="5"/>
      <path d="M8,27 L16,0 M18,27 L10,0"/>
    </g>
  </svg>
</section>

<section class="ad ad--landscape-b" aria-label="Anzeige Ruhepunkt Sana, Variante mit Gutschein oben">
  <svg viewBox="0 0 707 392" xmlns="http://www.w3.org/2000/svg">
    <defs>
      <linearGradient id="photoFadeB" x1="0" x2="1">
        <stop offset="0" stop-color="var(--white)"/>
        <stop offset=".35" stop-color="var(--photo-light)"/>
        <stop offset="1" stop-color="var(--photo-mid)"/>
      </linearGradient>
      <linearGradient id="bandTopB" x1="0" x2="1">
        <stop offset="0" stop-color="var(--green)" stop-opacity="0"/>
        <stop offset=".45" stop-color="var(--green)"/>
        <stop offset="1" stop-color="var(--green)"/>
      </linearGradient>
      <linearGradient id="bandCtaB" x1="0" x2="1">
        <stop offset="0" stop-color="var(--green)"/>
        <stop offset=".7" stop-color="var(--green)"/>
        <stop offset="1" stop-color="var(--green)" stop-opacity="0"/>
      </linearGradient>
    </defs>

    <rect class="photo" x="290" y="0" width="417" height="392" fill="url(#photoFadeB)" role="img" aria-label="Foto: Frau auf dem Bett sitzend, die sich den schmerzenden Rücken hält"/>
    <rect x="370" y="0" width="337" height="62" fill="url(#bandTopB)"/>
    <text class="voucher-title" x="668" y="32" text-anchor="end">GUTSCHEIN</text>
    <text class="voucher-sub" x="677" y="54" text-anchor="end">KOSTENLOSE LIEGEDRUCK-MESSUNG</text>
    <g class="scissors scissors--light" transform="translate(680,9) scale(.8)" aria-hidden="true">
      <circle cx="6" cy="32" r="5"/><circle cx="20" cy="32" r="5"/>
      <path d="M8,27 L16,0 M18,27 L10,0"/>
    </g>

    <text class="brand" x="37" y="118">Ruhepunkt Sana</text>

    <text class="headline" x="30" y="182"><tspan class="hl-green" font-size="46">Na,</tspan><tspan class="hl-green" font-size="32"> mal </tspan><tspan class="hl-maroon" font-size="42">wieder</tspan></text>
    <text class="headline hl-maroon" x="30" y="227" font-size="52">schlecht</text>
    <text class="headline hl-green" x="30" y="268" font-size="40">geschlafen?</text>

    <path d="M0,286 H370 C395,286 415,300 405,322 H0 Z" fill="url(#bandCtaB)"/>
    <path class="wave" d="M0,322 C220,328 360,318 450,278 C545,238 630,233 707,226 V392 H0 Z" fill="var(--maroon)"/>
    <text class="cta" x="30" y="310">DANN KOMMEN SIE ZU UNS!</text>

    <circle cx="597" cy="160" r="65" fill="var(--maroon)"/>
    <text class="slogan" transform="translate(597,160) rotate(-12)" text-anchor="middle"><tspan x="0" y="-4">Wir nehmen</tspan><tspan x="0" y="24">uns Zeit!</tspan></text>

    <text class="address" x="679" y="284" text-anchor="end">Lindenallee 8</text>
    <text class="address" x="679" y="318" text-anchor="end">23840 Lindenau</text>
    <text class="phone" x="679" y="364" text-anchor="end">04531 48 26 90</text>

    <text class="tag-spaced" x="32" y="364">ERGONOMISCHE BETTEN</text>
  </svg>
</section>

</body>
</html>
```